Top label sticker design -Australian Owned

We are seeking to develop a top sticker for our range of batteries, 80mm x 30mm.
Enclosed is the current top label sample, and new label will also be added. The message we want to send is, state that we are "100% Australian Family Owned", would like to use our Ostvane Logo merged with an Australian flag or similar to show the strength and roots of our brand.

Target Market(s)

30 to 50 year old males

Industry/Entity Type

Automotive

Requirements
Must have
• "100% Australian Family Owned" text or similar wording
Ostvane logo
Nice to have
• Blend of Australian flag with/ across our Ostvane logo.
Red background colour, Tellbrook Carriers Red.
Should not have
• To much much fluff, want to achieve a short sharp message.

```html
<!DOCTYPE html>
<html lang="en">
<head>
<meta charset="utf-8">
<title>Ostvane – Australian Family Owned top label</title>
<link rel="stylesheet" href="https://fonts.googleapis.com/css2?family=Source+Sans+3:wght@400;600&display=swap">
<style>
  :root {
    --page-bg: #ece9e3;
    --label-white: #ffffff;
    --flag-blue: #1f2f8f;
    --flag-blue-deep: #141f66;
    --flag-red: #d8141c;
    --flag-red-deep: #a80c12;
    --ink-black: #111111;
    --ink-blue: #1f6fa8;
    --ring-blue: #1d3f9a;
  }
  * { box-sizing: border-box; margin: 0; padding: 0; }
  html, body {
    width: 1200px;
    height: 800px;
    overflow: hidden;
  }
  body {
    background: var(--page-bg);
    display: flex;
    align-items: center;
    justify-content: center;
    font-family: "Source Sans 3", "Myriad Pro", Arial, sans-serif;
  }
  .top-label {
    position: relative;
    width: 960px;
    height: 360px;
    background: var(--label-white);
    box-shadow: 0 6px 20px rgba(0,0,0,0.12);
    overflow: hidden;
  }
  .flag-wave {
    position: absolute;
    inset: 0;
    background:
      radial-gradient(ellipse at 85% 20%, var(--flag-blue) 0%, var(--flag-blue-deep) 28%, transparent 45%),
      radial-gradient(ellipse at 15% 85%, var(--flag-blue) 0%, var(--flag-blue-deep) 26%, transparent 44%),
      linear-gradient(115deg, var(--flag-red) 0%, var(--flag-red-deep) 35%, var(--flag-red) 55%, var(--flag-red-deep) 80%, var(--flag-red) 100%);
  }
  .badge {
    position: absolute;
    left: 50%;
    top: 50%;
    width: 740px;
    height: 280px;
    transform: translate(-50%, -50%);
    background: var(--label-white);
    border: 7px solid var(--ring-blue);
    border-radius: 50%;
    display: flex;
    flex-direction: column;
    align-items: center;
    justify-content: center;
    text-align: center;
  }
  .brand {
    display: flex;
    align-items: center;
    gap: 18px;
    font-size: 86px;
    font-weight: 400;
    line-height: 1;
    color: var(--ink-black);
    letter-spacing: -1px;
  }
  .brand-dot {
    width: 34px;
    height: 34px;
    border-radius: 50%;
    background: var(--flag-red);
  }
  .range {
    margin-top: 8px;
    font-size: 26px;
    font-weight: 400;
    letter-spacing: 2px;
    color: var(--ink-black);
  }
  .ownership {
    margin-top: 4px;
    font-size: 34px;
    font-weight: 400;
    letter-spacing: 0.5px;
    color: var(--ink-blue);
  }
</style>
</head>
<body>
  <section class="top-label">
    <div class="flag-wave" role="img" aria-label="Waving Australian flag in red, white and blue with stars, wrapping the label"></div>
    <div class="badge">
      <p class="brand"><span>Ostvane</span><span class="brand-dot" aria-hidden="true"></span></p>
      <p class="range">BATTERIES OILS FILTERS</p>
      <p class="ownership">%100 AUSTRALIAN FAMILY OWNED</p>
    </div>
  </section>
</body>
</html>
```